Banner Ad Design job - Bramblet Mortgage - Banner Ads for Re-Marketing Campaigns

Need a banner ad for a retargeting Campaign with Velvet Reach.

We would like to incorporate our attached logo. Also would like to incorporate a call to action "Pre-Qualify for a home loan today" and a button to click. This banner is to encourage previous customers to come back to our website and submit information. It must look good on mobile and desktop.

Our website is BrambletMortgage.example

Target Market(s)

Customers Seeking a Mortgage Loan

Industry/Entity Type

Mortgage Lender

Colors

Designer to choose colors to be used in the design.

Requirements
Must have
• - We would like the same basic design in the 4 sizes below.
• - 728x90 pixels leader board
• - 300x250 medium rectangle
• - 300x600 half page
• - 600x315 chatterbook
Nice to have
• Call to action. Click button or Something to promote them to click through
Should not have
• We are Open

```html
<!DOCTYPE html>
<html lang="en">
<head>
<meta charset="utf-8">
<title>Bramblet Mortgage – Pre-Qualify Leaderboard</title>
<link rel="stylesheet" href="https://fonts.googleapis.com/css2?family=Open+Sans:wght@400;700&display=swap">
<style>
  :root {
    --brand-ink: #3a4148;
    --brand-dot: #2f7fc1;
    --panel-white: #ffffff;
    --headline-white: #ffffff;
    --cta-orange: #f6a11a;
    --cta-text: #2a2a2a;
    --scene-sky: #8a9298;
    --scene-shore: #6c747a;
    --scene-sea: #5d6e7a;
    --scene-shade: rgba(30, 36, 42, 0.45);
  }
  * { box-sizing: border-box; margin: 0; padding: 0; }
  html, body {
    width: 1200px;
    height: 148px;
    overflow: hidden;
    background: #ffffff;
  }
  .leaderboard {
    position: relative;
    width: 1200px;
    height: 148px;
    display: flex;
    font-family: "Open Sans", Arial, sans-serif;
  }
  .brand-panel {
    width: 293px;
    height: 100%;
    background: var(--panel-white);
    display: flex;
    align-items: center;
    justify-content: center;
    gap: 10px;
    padding: 0 16px;
  }
  .brand-mark {
    width: 14px;
    height: 14px;
    background: var(--brand-dot);
    flex: none;
  }
  .brand-name {
    color: var(--brand-ink);
    font-weight: 400;
    font-size: 21px;
    line-height: 1;
    white-space: nowrap;
  }
  .hero {
    position: relative;
    flex: 1;
    height: 100%;
    display: flex;
    align-items: center;
    justify-content: space-between;
    padding: 0 33px 0 20px;
    overflow: hidden;
  }
  .hero-scene {
    position: absolute;
    inset: 0;
    background:
      linear-gradient(var(--scene-shade), var(--scene-shade)),
      linear-gradient(100deg, var(--scene-sky) 0%, #9aa0a4 30%, var(--scene-shore) 62%, var(--scene-sea) 100%);
  }
  .headline {
    position: relative;
    color: var(--headline-white);
    font-weight: 400;
    font-size: 33px;
    letter-spacing: -0.2px;
    white-space: nowrap;
  }
  .cta-button {
    position: relative;
    display: flex;
    align-items: center;
    justify-content: center;
    gap: 8px;
    width: 178px;
    height: 53px;
    background: var(--cta-orange);
    color: var(--cta-text);
    font-weight: 700;
    font-size: 16px;
    letter-spacing: 0.4px;
    text-decoration: none;
  }
  .cta-arrow { width: 9px; height: 12px; }
</style>
</head>
<body>
  <div class="leaderboard">
    <div class="brand-panel">
      <span class="brand-mark" aria-hidden="true"></span>
      <span class="brand-name">Bramblet Mortgage</span>
    </div>
    <div class="hero">
      <div class="hero-scene" role="img" aria-label="Photo of a seaside row of homes along a beach with waves at dusk"></div>
      <p class="headline">Pre–Qualify for a home loan today!</p>
      <a class="cta-button" href="#">
        CLICK HERE
        <svg class="cta-arrow" viewBox="0 0 9 12" aria-hidden="true"><path d="M1 0 L9 6 L1 12 Z" fill="currentColor"/></svg>
      </a>
    </div>
  </div>
</body>
</html>
```